plumAxis-rt

KelvaroArchitecturalhub.example
go to site for additional information, we sell Kelvaro TR-VEX architectural finishes for interior wall, column, furniture, doors

phone numbers: 800-555-0147 / 847-555-0192 / 414-555-0163
Names for cards: Peter Lorne / Owen Falk

Industry/Entity Type

Furniture

Contact Information for Business Card

plumAxis architectural graphics, Kelvaro TR-VEX Architectural interior finishes, velmira glass finishes, dichroic glass finishes. Peter Lorne,
midwestern territories

```html
<!DOCTYPE html>
<html lang="en">
<head>
<meta charset="utf-8">
<title>PlumAxis-RT Business Card</title>
<link rel="stylesheet" href="https://fonts.googleapis.com/css2?family=Cinzel:wght@500&family=Questrial&display=swap">
<style>
  :root {
    --page-bg: #e6e7e9;
    --card-white: #ffffff;
    --card-shade: #eef0f1;
    --teal: #4fb3b7;
    --teal-deep: #2f9aa0;
    --swoosh-dark: #5a5d62;
    --swoosh-light: #c9cbce;
    --ink: #2f3236;
    --on-teal: #ffffff;
  }
  * { margin: 0; padding: 0; box-sizing: border-box; }
  html, body {
    width: 1200px; height: 900px; overflow: hidden;
    background: var(--page-bg);
  }
  .business-card {
    position: absolute; left: 100px; top: 164px;
    width: 1000px; height: 572px;
    border-radius: 48px; overflow: hidden;
    background: linear-gradient(135deg, var(--card-white) 40%, var(--card-shade));
    box-shadow: 0 18px 40px rgba(0,0,0,0.18);
  }
  .card-art { position: absolute; inset: 0; width: 100%; height: 100%; }
  .brand-name {
    position: absolute; left: 520px; top: 170px;
    font-family: "Cinzel", serif; font-weight: 500;
    font-size: 58px; letter-spacing: 1px; color: var(--teal-deep);
  }
  .holder {
    position: absolute; left: 560px; top: 345px; width: 300px;
    text-align: center; font-family: "Questrial", sans-serif; color: var(--ink);
  }
  .holder-name { font-size: 30px; letter-spacing: 1px; }
  .holder-role { font-size: 25px; margin-top: 2px; }
  .contact-list {
    position: absolute; left: 34px; top: 268px; list-style: none;
    font-family: "Questrial", sans-serif; font-size: 16px; color: var(--on-teal);
  }
  .contact-list li { display: flex; align-items: center; gap: 10px; height: 29px; white-space: nowrap; }
  .contact-icon {
    width: 18px; height: 18px; border-radius: 50%; flex: none;
    background: var(--on-teal); display: flex; align-items: center; justify-content: center;
  }
  .contact-icon svg { width: 11px; height: 11px; }
</style>
</head>
<body>
  <div class="business-card">
    <svg class="card-art" viewBox="0 0 1000 572" aria-hidden="true">
      <defs>
        <linearGradient id="swooshFill" x1="0" y1="0" x2="1" y2="0">
          <stop offset="0" stop-color="var(--swoosh-light)"/>
          <stop offset="0.5" stop-color="var(--swoosh-dark)"/>
          <stop offset="1" stop-color="var(--swoosh-light)"/>
        </linearGradient>
        <linearGradient id="tealFill" x1="0" y1="0" x2="1" y2="1">
          <stop offset="0" stop-color="var(--teal-deep)"/>
          <stop offset="1" stop-color="var(--teal)"/>
        </linearGradient>
      </defs>
      <path class="teal-band" fill="url(#tealFill)"
        d="M0,160 C190,160 300,330 470,420 C640,505 820,525 1000,520 L1000,572 L0,572 Z"/>
      <path class="teal-edge" fill="none" stroke="var(--card-white)" stroke-width="6"
        d="M0,152 C190,152 300,322 470,412 C640,497 820,517 1000,512"/>
      <path class="grey-swoosh" fill="url(#swooshFill)"
        d="M0,98 C220,98 330,320 520,392 C660,444 790,456 890,452 C770,478 630,470 500,424 C320,356 220,126 0,120 Z"/>
    </svg>

    <div class="brand-name">PlumAxis-RT</div>

    <div class="holder">
      <div class="holder-name">PETER LORNE</div>
      <div class="holder-role">Managing Director</div>
    </div>

    <ul class="contact-list">
      <li><span class="contact-icon"><svg viewBox="0 0 12 12"><path d="M3 1 L5 3 L4 5 Q5 7 7 8 L9 7 L11 9 L9.5 11 Q4 10 1 3 Z" fill="var(--teal-deep)"/></svg></span>800-555-0147</li>
      <li><span class="contact-icon"><svg viewBox="0 0 12 12"><path d="M3 1 L5 3 L4 5 Q5 7 7 8 L9 7 L11 9 L9.5 11 Q4 10 1 3 Z" fill="var(--teal-deep)"/></svg></span>847-555-0192</li>
      <li><span class="contact-icon"><svg viewBox="0 0 12 12"><rect x="1" y="3" width="10" height="7" fill="var(--teal-deep)"/><path d="M1 3 L6 7 L11 3" stroke="var(--on-teal)" fill="none"/></svg></span>peter@plumaxis.example</li>
      <li><span class="contact-icon"><svg viewBox="0 0 12 12"><circle cx="6" cy="6" r="4.5" fill="none" stroke="var(--teal-deep)" stroke-width="1.4"/><path d="M1.5 6 H10.5 M6 1.5 V10.5" stroke="var(--teal-deep)" stroke-width="1"/></svg></span>KelvaroArchitecturalhub.example</li>
      <li><span class="contact-icon"><svg viewBox="0 0 12 12"><path d="M6 11 C3 7 2.5 5.5 2.5 4.5 A3.5 3.5 0 0 1 9.5 4.5 C9.5 5.5 9 7 6 11 Z" fill="var(--teal-deep)"/></svg></span>27 Tenth Floor, Harlow Bend Way</li>
    </ul>
  </div>
</body>
</html>
```